Sport Celebration Day Poster

The poster should highlight the sport of archery and bring awareness to the sport and invite people to come and try archery. We have a logo that must be featured, as well as a sample photos that can be used in the creative process, but do not necessarily have to be featured. The feel of the poster should be fun and inviting and have archery imagery (bows, arrows, targets, etc.).

The poster must feature the date MAY 11, 2019 and "Try Archery."

We would like to see an area where our sport clubs can fill in their own information including sections for "Name, Date, Location, Times, Location, Email, Website, and Notes."

Submissions should include some of these colours or colours from the logo:
Blue #00A1EF, Grey #313A43, Green #406C1D, Red #DC2F31, Yellow #FDDD39

```html
<!DOCTYPE html>
<html lang="en">
<head>
<meta charset="utf-8">
<title>Try Archery – May 11, 2019</title>
<link rel="stylesheet" href="https://fonts.googleapis.com/css2?family=Rye&family=Tinos&family=Arimo:wght@700&display=swap">
<style>
  :root {
    --yellow: #FDDD39;
    --red: #DC2F31;
    --red-dark: #8E1A1C;
    --white: #FFFFFF;
    --blue: #00A1EF;
    --blue-dark: #0068A0;
    --green: #406C1D;
    --green-dark: #1F3A0C;
    --grey: #313A43;
    --badge: #D9D9D9;
  }
  * { margin: 0; padding: 0; box-sizing: border-box; }
  html, body { width: 849px; height: 1200px; overflow: hidden; background: var(--white); }
  .poster {
    position: relative;
    width: 849px;
    height: 1200px;
    background: var(--yellow);
    overflow: hidden;
    font-family: "Tinos", "Times New Roman", serif;
  }
  .event-mark {
    position: absolute;
    left: 290px;
    top: 80px;
    display: flex;
    align-items: center;
    gap: 14px;
    color: var(--red);
    font-size: 46px;
    line-height: 1;
  }
  .event-mark .dot {
    width: 38px; height: 38px; border-radius: 50%;
    background: var(--red);
  }
  .target, .headline {
    position: absolute;
    left: 0; top: 0;
  }
  .event-date {
    position: absolute;
    right: 154px;
    top: 410px;
    font-family: "Arimo", Arial, sans-serif;
    font-weight: 700;
    font-size: 43px;
    line-height: 1;
    color: var(--green);
    -webkit-text-stroke: 1.5px var(--green-dark);
    letter-spacing: 0.5px;
  }
  .club-form {
    position: absolute;
    left: 259px;
    top: 489px;
    width: 330px;
    list-style: none;
  }
  .club-form li {
    height: 35.4px;
    padding: 0 5px;
    color: var(--white);
    font-size: 26px;
    line-height: 35px;
  }
  .club-form li:nth-child(odd) { background: var(--red); }
  .federation-mark {
    position: absolute;
    left: 18px;
    top: 1012px;
    display: flex;
    align-items: center;
    gap: 10px;
    color: var(--red);
    font-size: 30px;
    line-height: 1;
  }
  .federation-mark .dot {
    width: 26px; height: 26px; border-radius: 50%;
    background: var(--red);
  }
  .partner-band {
    position: absolute;
    left: 0; bottom: 0;
    width: 849px;
    height: 139px;
    background: var(--white);
    display: flex;
    align-items: center;
    justify-content: space-around;
    padding: 0 20px;
  }
  .partner-badge { background: var(--badge); }
  .partner-badge.round { width: 90px; height: 90px; border-radius: 50%; }
  .partner-badge.tall { width: 62px; height: 94px; border-radius: 30px; }
  .partner-badge.wide { width: 232px; height: 56px; }
  .partner-badge.mid { width: 150px; height: 88px; }
  .partner-badge.small { width: 118px; height: 82px; }
</style>
</head>
<body>
<main class="poster">
  <div class="event-mark"><span class="dot"></span><span>Bullseye Day</span></div>

  <svg class="target" width="849" height="1200" viewBox="0 0 849 1200" aria-hidden="true">
    <defs>
      <radialGradient id="ringRed" cx="50%" cy="45%" r="55%">
        <stop offset="85%" stop-color="var(--red)"/>
        <stop offset="100%" stop-color="var(--red-dark)"/>
      </radialGradient>
      <radialGradient id="ringWhite" cx="50%" cy="45%" r="55%">
        <stop offset="88%" stop-color="#FFFFFF"/>
        <stop offset="100%" stop-color="#C9C9C9"/>
      </radialGradient>
      <radialGradient id="bullBlue" cx="50%" cy="40%" r="60%">
        <stop offset="80%" stop-color="var(--blue)"/>
        <stop offset="100%" stop-color="var(--blue-dark)"/>
      </radialGradient>
    </defs>
    <circle class="ring-outer" cx="424" cy="600" r="390" fill="url(#ringRed)"/>
    <circle class="ring-middle" cx="424" cy="598" r="330" fill="url(#ringWhite)"/>
    <circle class="ring-bull" cx="424" cy="600" r="264" fill="url(#bullBlue)"/>
  </svg>

  <svg class="headline" width="849" height="1200" viewBox="0 0 849 1200" role="img" aria-label="Try Archery">
    <text x="422" y="388" text-anchor="middle" transform="rotate(-6 422 360)"
          font-family="Rye, serif" font-size="76" textLength="545" lengthAdjust="spacingAndGlyphs"
          fill="var(--green)" stroke="var(--green-dark)" stroke-width="2.5">TRY ARCHERY</text>
  </svg>

  <p class="event-date">MAY 11, 2019</p>

  <ul class="club-form">
    <li>Name:</li>
    <li>Date:</li>
    <li>Location:</li>
    <li>Time:</li>
    <li>Email:</li>
    <li>Website:</li>
    <li>Notes:</li>
  </ul>

  <div class="federation-mark"><span class="dot"></span><span>Arrowline Federation</span></div>

  <footer class="partner-band">
    <div class="partner-badge tall"></div>
    <div class="partner-badge round"></div>
    <div class="partner-badge wide"></div>
    <div class="partner-badge mid"></div>
    <div class="partner-badge small"></div>
  </footer>
</main>
</body>
</html>
```